Coral Tandem
Stewardship for Harbors
Thank you all for the great designs that you submitted!
On the designs, I prefer to not have a vertical line on the card that separates information like on #73. I prefer for the information to be naturally separated by the design like on #65.
For the back of the card, so far, I prefer the ones that use the logo as sort of a watermark such as #43, #102, #119.
I'm also not too fond of the cards with lots of black on them. Some for a highlight is good but for a background, I'd prefer not to have black. So I'm eliminating those as well.
Thank you all for lots of great designs. I prefer the ones that use some kind of wave look on the front. So I've eliminated the ones that have more of a block or squarish look. I'm also eliminating most of the ones that have the logo mark above or below the lettering of the logo as I want to retain the consistency of the logo with the mark to the left of the lettering.
My preference on the front of the card is to retain the logo design with the mark to the left of CoralTandem and not move it above or below the lettering.
This project is for both business card and stationary, so please include stationary and envelop design with the business cards. Thanks.

```html
<!DOCTYPE html>
<html lang="en">
<head>
<meta charset="utf-8">
<title>Coral Tandem — Business Cards</title>
<link href="https://fonts.googleapis.com/css2?family=Open+Sans:wght@400;600&family=Ubuntu:wght@500&display=swap" rel="stylesheet">
<style>
  :root {
    --stage: #e9e6e1;
    --card-white: #ffffff;
    --card-grey: #d3d4d6;
    --brand-red: #c8102e;
    --brand-red-dark: #8e0a1f;
    --ink: #4a4a4c;
    --ink-soft: #6d6e70;
    --line-grey: #b9babc;
    --on-red: #ffffff;
  }
  * { box-sizing: border-box; margin: 0; padding: 0; }
  html, body { width: 1200px; height: 804px; overflow: hidden; }
  body { background: var(--stage); font-family: "Open Sans", Arial, sans-serif; position: relative; }

  .card { position: absolute; width: 499px; height: 288px; overflow: hidden; box-shadow: 0 2px 6px rgba(0,0,0,.18); }
  .card--front { left: 96px; top: 96px; background: var(--card-white); }
  .card--back { left: 629px; top: 96px; background: var(--card-white); }
  .card--reverse { left: 343px; top: 432px; width: 509px; height: 295px; background: var(--card-grey); }

  .wordmark { position: absolute; display: flex; align-items: center; gap: 12px; white-space: nowrap; }
  .wordmark__dot { width: 46px; height: 46px; border-radius: 50%; background: var(--brand-red); flex: none; }
  .wordmark__name { font-family: "Ubuntu", "Open Sans", sans-serif; font-weight: 500; font-size: 48px; color: var(--ink); letter-spacing: -1px; line-height: 1; }

  .holder { position: absolute; top: 24px; left: 0; right: 0; text-align: center; font-size: 13px; color: var(--ink); }
  .holder__name { font-weight: 600; }
  .holder__sep { color: var(--line-grey); margin: 0 8px; }
  .holder__role { font-size: 11px; }

  .front__wordmark { left: 30px; top: 74px; }
  .front__wave { position: absolute; left: 0; top: 0; width: 499px; height: 288px; }

  .address { position: absolute; left: 44px; top: 238px; color: var(--on-red); font-size: 11px; line-height: 22px; }
  .contacts { position: absolute; left: 192px; top: 214px; list-style: none; color: var(--on-red); font-size: 11px; line-height: 22px; }
  .contacts li { display: flex; align-items: center; gap: 8px; }
  .contacts svg { width: 10px; height: 10px; fill: var(--on-red); }

  .watermark { position: absolute; border-radius: 50%; background: var(--brand-red); opacity: .07; }
  .back__watermark { width: 210px; height: 210px; left: 138px; top: 22px; }
  .back__wordmark { left: 44px; top: 112px; }
  .site { position: absolute; left: 0; right: 0; text-align: center; font-size: 11px; letter-spacing: 1px; color: var(--ink-soft); }
  .back__site { top: 240px; }

  .reverse__wordmark { left: 50%; top: 98px; transform: translateX(-50%); }
  .reverse__wordmark .wordmark__dot { width: 60px; height: 60px; }
  .reverse__wordmark .wordmark__name { font-size: 30px; }
  .reverse__site { top: 244px; color: var(--ink); }
</style>
</head>
<body>

  <section class="card card--front" aria-label="Business card front">
    <svg class="front__wave" viewBox="0 0 499 288" aria-hidden="true">
      <defs>
        <linearGradient id="redBand" x1="0" y1="0" x2="1" y2="1">
          <stop offset="0" stop-color="#d4152f"/>
          <stop offset="1" stop-color="#8e0a1f"/>
        </linearGradient>
      </defs>
      <path d="M0 160 C150 168 330 190 499 206" fill="none" stroke="#b9babc" stroke-width="2"/>
      <path d="M0 170 C160 178 330 196 499 214 L499 288 L0 288 Z" fill="url(#redBand)"/>
      <path d="M0 172 C160 180 330 198 499 216" fill="none" stroke="#e84a5f" stroke-width="1.5" opacity=".7"/>
    </svg>

    <p class="holder"><span class="holder__name">Dr. Rowan Kessler</span><span class="holder__sep">|</span><span class="holder__role">Executive Director</span></p>

    <div class="wordmark front__wordmark">
      <span class="wordmark__dot"></span>
      <span class="wordmark__name">CoralTandem</span>
    </div>

    <p class="address">PO Box 318402<br>Dayton, OH 45402</p>
    <ul class="contacts">
      <li><svg viewBox="0 0 10 10"><path d="M2 0h2l1 3-1.5 1a6 6 0 0 0 2.5 2.5L7 5l3 1v2a2 2 0 0 1-2 2A8 8 0 0 1 0 2 2 2 0 0 1 2 0z"/></svg>555-014-2290</li>
      <li><svg viewBox="0 0 10 10"><path d="M0 2h10v6H0z M0 2l5 3 5-3"/></svg>rkessler@coral-tandem.org</li>
      <li><svg viewBox="0 0 10 10"><circle cx="5" cy="5" r="4.5"/></svg>www.coral-tandem.org</li>
    </ul>
  </section>

  <section class="card card--back" aria-label="Business card back">
    <span class="watermark back__watermark"></span>
    <div class="wordmark back__wordmark">
      <span class="wordmark__dot"></span>
      <span class="wordmark__name">CoralTandem</span>
    </div>
    <p class="site back__site">www.coral-tandem.org</p>
  </section>

  <section class="card card--reverse" aria-label="Business card reverse">
    <div class="wordmark reverse__wordmark">
      <span class="wordmark__dot"></span>
      <span class="wordmark__name">CoralTandem</span>
    </div>
    <p class="site reverse__site">www.coral-tandem.org</p>
  </section>

</body>
</html>
```